Bright, Fun and hard to forget home inspection business card.

We need a Business card design for a new Home Inspection company. We are building a brand that is bright, fun and easy to remember.

Target Market(s)

Anyone involed in buying and selling of homes.

Industry/Entity Type

Home Inspection

Contact Information for Business Card

Colin Hartwell Owner/Inspector

Wedsite- KestrelHouseCheck.example
Phone: 253-555-0147
Email- ColinHartwell@mailbox.example
WA Lic # 4738

Requirements
Must have
• BQRV LOGO somewhere on card.

```html
<!DOCTYPE html>
<html lang="en">
<head>
<meta charset="utf-8">
<title>Kestrel House Check – Business Card</title>
<link href="https://fonts.googleapis.com/css2?family=Saira:wght@400;600&display=swap" rel="stylesheet">
<style>
  :root {
    --backdrop: #d7dadf;
    --card: #f2f2f2;
    --card-shade: #dcdcdc;
    --charcoal: #3a3a3a;
    --ink: #333333;
    --orange: #f05a28;
    --white: #ffffff;
  }
  * { margin: 0; padding: 0; box-sizing: border-box; }
  html, body {
    width: 1200px; height: 866px; overflow: hidden;
    background: var(--backdrop);
    font-family: "Saira", sans-serif;
  }
  .stage { position: relative; width: 1200px; height: 866px; }
  .card {
    position: absolute;
    width: 540px; height: 309px;
    background: radial-gradient(ellipse at 45% 45%, var(--white) 0%, var(--card) 55%, var(--card-shade) 100%);
    box-shadow: 0 6px 18px rgba(0,0,0,0.18);
    overflow: hidden;
  }
  .card--front { left: 40px; top: 278px; }
  .card--back { left: 620px; top: 278px; }

  .brand {
    display: flex; align-items: center; gap: 10px;
    color: var(--orange); font-weight: 600;
    text-transform: uppercase; line-height: 1.05;
  }
  .brand__dot { border-radius: 50%; background: var(--orange); flex: none; }
  .card--front .brand {
    position: absolute; left: 50%; top: 50%;
    transform: translate(-50%, -50%);
    font-size: 34px;
  }
  .card--front .brand__dot { width: 30px; height: 30px; }
  .card--back .brand {
    position: absolute; left: 40px; top: 120px;
    font-size: 19px; gap: 7px;
  }
  .card--back .brand__dot { width: 16px; height: 16px; }

  .wave { position: absolute; inset: 0; width: 540px; height: 309px; }
  .wave__dark { fill: var(--charcoal); }
  .wave__accent { fill: var(--orange); }

  .person { position: absolute; right: 28px; top: 30px; text-align: right; color: var(--ink); }
  .person__name { font-size: 17px; font-weight: 600; letter-spacing: 1px; text-transform: uppercase; }
  .person__role { font-size: 12px; margin-top: -2px; }

  .address { position: absolute; right: 28px; top: 128px; text-align: right; color: var(--white); font-size: 11.5px; line-height: 1.35; }
  .website { position: absolute; right: 28px; top: 196px; color: var(--white); font-size: 11.5px; }

  .contacts { position: absolute; left: 22px; bottom: 16px; list-style: none; color: var(--white); font-size: 11px; }
  .contacts li { display: flex; align-items: center; gap: 8px; height: 17px; }
  .contacts svg { width: 11px; height: 11px; fill: var(--white); flex: none; }
</style>
</head>
<body>
<main class="stage">
  <section class="card card--front" aria-label="Card front">
    <div class="brand"><span class="brand__dot"></span><span>Kestrel House<br>Check LLC</span></div>
  </section>

  <section class="card card--back" aria-label="Card back">
    <svg class="wave" viewBox="0 0 540 309" aria-hidden="true">
      <path class="wave__accent" d="M0,218 C180,198 380,132 540,42 C390,140 190,212 0,232 Z"/>
      <path class="wave__dark" d="M0,236 C190,216 390,150 540,58 L540,309 L0,309 Z"/>
    </svg>

    <div class="brand"><span class="brand__dot"></span><span>Kestrel House<br>Check LLC</span></div>

    <div class="person">
      <p class="person__name">Marcus Dellow</p>
      <p class="person__role">Managing Director</p>
    </div>

    <p class="address">041.12th floor,Mill<br>Harbour Road KVT</p>
    <p class="website">www.yoursitename.example</p>

    <ul class="contacts">
      <li><svg viewBox="0 0 24 24"><path d="M6.6 10.8a15 15 0 0 0 6.6 6.6l2.2-2.2a1 1 0 0 1 1-.25 11 11 0 0 0 3.6.6 1 1 0 0 1 1 1V20a1 1 0 0 1-1 1A17 17 0 0 1 3 4a1 1 0 0 1 1-1h3.5a1 1 0 0 1 1 1c0 1.25.2 2.45.6 3.6a1 1 0 0 1-.25 1z"/></svg>012 555 0189</li>
      <li><svg viewBox="0 0 24 24"><path d="M7 1h10a2 2 0 0 1 2 2v18a2 2 0 0 1-2 2H7a2 2 0 0 1-2-2V3a2 2 0 0 1 2-2zm0 3v14h10V4zm5 15.5a1 1 0 1 0 0 2 1 1 0 0 0 0-2z"/></svg>012 555 0189</li>
      <li><svg viewBox="0 0 24 24"><path d="M6 2h10v5H6zM3 8h18v12H3zm3 3v2h4v-2zm0 4v2h4v-2zm8-4v6h4v-6z"/></svg>012 555 0189</li>
      <li><svg viewBox="0 0 24 24"><path d="M2 5h20v14H2zm2 2v.5l8 5.5 8-5.5V7zm0 3v7h16v-7l-8 5.5z"/></svg>yourname@mail.example</li>
    </ul>
  </section>
</main>
</body>
</html>
```